Web Design Project for SEARCH ENGINE !

We need a website design for torrents search engine.

The Website will be www.Qorvexa.com

Qorvexa is a a search engine for torrents.
Qorvexa search and index torrents results from all torrents sites.

We will need:
Logo
WebSite Design
slogen (optional)

we need only PSDs - no codded pages are needed !

Design to the following screen Size & resolution: 1024 x 768

***PLEASE DOWNLOAD ATTACHED FILE !

```html
<!DOCTYPE html>
<html lang="en">
<head>
<meta charset="utf-8">
<title>Qorvexa – Torrent Search</title>
<link rel="stylesheet" href="https://fonts.googleapis.com/css2?family=PT+Sans:wght@400;700&family=Arimo:ital@1&display=swap">
<style>
  :root {
    --link-blue: #1f5fb0;
    --brand-blue: #3b8fd2;
    --button-blue: #2f86cc;
    --button-blue-dark: #1f6fb2;
    --rule: #8fa9c9;
    --field-border: #4b95d6;
    --placeholder: #9a9a9a;
    --ink: #111111;
    --page: #ffffff;
    --divider: #3a6db5;
  }
  * { box-sizing: border-box; margin: 0; padding: 0; }
  html, body { width: 1200px; height: 800px; overflow: hidden; background: var(--page); }
  body { position: relative; font-family: "PT Sans", "Myriad Pro", sans-serif; color: var(--ink); }
  a { color: var(--link-blue); }

  .site-header {
    position: absolute; left: 0; top: 0; width: 1200px; height: 52px;
    border-bottom: 1px solid var(--rule);
  }
  .main-nav {
    position: absolute; left: 49px; top: 26px;
    display: flex; gap: 17px; font-size: 15.5px;
  }
  .main-nav a { text-decoration: underline; }
  .main-nav .more { display: inline-flex; align-items: center; gap: 5px; }
  .account-bar {
    position: absolute; right: 44px; top: 26px;
    display: flex; align-items: center; font-size: 15.5px;
  }
  .language { display: inline-flex; align-items: center; gap: 10px; margin-right: 56px; }
  .language-flag { width: 25px; height: 15px; display: block; }
  .account-bar .sep { color: var(--link-blue); margin: 0 14px; }

  .brand {
    position: absolute; left: 0; width: 1200px; top: 208px;
    display: flex; justify-content: center; align-items: center; gap: 14px;
    padding-left: 48px;
  }
  .brand-dot { width: 22px; height: 22px; border-radius: 50%; background: var(--brand-blue); }
  .brand-name {
    font-family: "PT Sans", sans-serif; font-weight: 700; font-size: 64px;
    color: var(--brand-blue); letter-spacing: 1px; line-height: 1;
  }

  .search-form {
    position: absolute; left: 270px; top: 318px; width: 712px; height: 48px;
    display: flex;
    border: 2px solid var(--field-border); border-radius: 24px;
    box-shadow: 0 3px 5px rgba(0,0,0,0.18);
    overflow: hidden; background: var(--page);
  }
  .search-input {
    flex: 1; border: 0; outline: 0; padding: 0 28px;
    font-family: "Arimo", Arial, sans-serif; font-style: italic; font-size: 24px;
    color: #333;
  }
  .search-input::placeholder { color: var(--placeholder); }
  .search-button {
    width: 68px; border: 0;
    background: linear-gradient(var(--button-blue), var(--button-blue-dark));
    display: flex; align-items: center; justify-content: center;
  }

  .site-footer { position: absolute; left: 0; top: 582px; width: 1200px; text-align: center; }
  .social-links { display: flex; justify-content: center; gap: 40px; margin-left: 14px; }
  .social-links span { width: 18px; height: 18px; border-radius: 3px; display: block; }
  .social-a { background: #3b5998; }
  .social-b { background: #333333; }
  .social-c { background: #2a6fa8; }
  .social-d { background: #4fb6e6; }
  .footer-links {
    margin-top: 14px; display: flex; justify-content: center; font-size: 15.5px; margin-left: 14px;
  }
  .footer-links a { text-decoration: none; }
  .footer-links .sep { color: var(--divider); margin: 0 19px; }
  .copyright { margin-top: 13px; font-size: 14.5px; line-height: 21px; margin-left: 14px; }
</style>
</head>
<body>
  <header class="site-header">
    <nav class="main-nav">
      <a href="#">Qorvexa</a>
      <a href="#">Film</a>
      <a href="#">Music</a>
      <a href="#">Game</a>
      <a href="#">Clip</a>
      <a href="#">Video</a>
      <a href="#">Top 100</a>
      <a href="#" class="more">More
        <svg width="12" height="8" viewBox="0 0 12 8"><path d="M0 0h12L6 8z" fill="var(--link-blue)"/></svg>
      </a>
    </nav>
    <div class="account-bar">
      <a href="#" class="language">
        <svg class="language-flag" viewBox="0 0 25 15" role="img" aria-label="Language flag">
          <rect width="25" height="15" fill="#2b3f8f"/>
          <rect x="10" width="5" height="15" fill="#ffffff"/>
          <rect y="5" width="25" height="5" fill="#ffffff"/>
          <rect x="11" width="3" height="15" fill="#c8202f"/>
          <rect y="6" width="25" height="3" fill="#c8202f"/>
        </svg>
        English
      </a>
      <a href="#">Log in</a>
      <span class="sep">|</span>
      <a href="#">Sign up</a>
    </div>
  </header>

  <div class="brand">
    <span class="brand-dot"></span>
    <span class="brand-name">Qorvexa</span>
  </div>

  <form class="search-form" action="#">
    <input class="search-input" type="text" placeholder="search...">
    <button class="search-button" type="submit" aria-label="Search">
      <svg width="26" height="26" viewBox="0 0 26 26">
        <circle cx="10" cy="10" r="7" fill="none" stroke="#fff" stroke-width="3"/>
        <line x1="15" y1="15" x2="23" y2="23" stroke="#fff" stroke-width="4" stroke-linecap="round"/>
      </svg>
    </button>
  </form>

  <footer class="site-footer">
    <div class="social-links">
      <span class="social-a" role="img" aria-label="Social network link"></span>
      <span class="social-b" role="img" aria-label="Social network link"></span>
      <span class="social-c" role="img" aria-label="Social network link"></span>
      <span class="social-d" role="img" aria-label="Social network link"></span>
    </div>
    <nav class="footer-links">
      <a href="#">Home</a><span class="sep">|</span>
      <a href="#">Privacy Policy</a><span class="sep">|</span>
      <a href="#">Terms of Use</a><span class="sep">|</span>
      <a href="#">Contact US</a>
    </nav>
    <p class="copyright">Copyright 2011 © Qorvexa.com<br>All rights reserved</p>
  </footer>
</body>
</html>
```